WTF!!! We need a modern professional website for a business litigation law firm.

We need a modern, clean, professional and uncomplicated website for a new business trial and litigation law firm called "Hallorand Trial Firm PLLC". Website must be mobile optimized for iPad and smartphone. The law firm specializes in counseling and representing large corporations, small businesses and entrepreneurs in and out of the courtroom. Lawyers in the firm serve as Florida counsel and trial counsel to organizations facing claims involving product liability, premises liability, professional liability, vehicle and transportation liability, warranty claims, construction defects and delay claims, complex business disputes, commercial litigation and bid disputes in State and Federal Courts. The website is mainly to provide information about the firm, and should include sections describing the firm, identifying the Industries Served and Areas of Practice ," a separate page identifying the "Professionals", a separate page for "Resources & Advisories," and a traveling "Connect With Us" button a site visitor can click on that will launch an email to the Firm's general email account. The website should allow us to easily modify the content on these pages, and let us add/modify links to external information sources. We will not sell anything or take payments through the website. We do need to be able to easily upload and update photographs of attorneys and add new attorneys names/email hyperlinks as the firm grows. We would like to add developments in the law or success stories easily and quickly, such as through a blog page. On the "Connect With Us" page the website should have hyperlinks to email the Firm, and there should be hyperlinks to email each professional on the "Professionals" page. The website should be viewable on mobile devices without distortion. The law firm focuses on trial work and should have some imagery associated with courtrooms, but the overall theme of the site should be modern, clean, and communicate sophistication and strength. The website should be made in Wordpress. We have uploaded logo files for Hallorand Trial Firm.

Target Market(s)

Corporations and companies that are looking for legal representation. Other attorneys/legal industry.

Industry/Entity Type

Legal Industry

Coding

Coded - Design and coding required

Number of Pages Required

1 page

Font styles to use
Sans Serif

Requirements
Must have
• Simple, clean, sophisticated, modern website that includes the logo, watermark of logo, and the elements described above.
Nice to have
• Pictures of city scape, buildings, courtroom, team members.

```html
<!DOCTYPE html>
<html lang="en">
<head>
<meta charset="utf-8">
<title>Hallorand Trial Firm</title>
<link href="https://fonts.googleapis.com/css2?family=Poppins:wght@300;400;500;600;700&display=swap" rel="stylesheet">
<style>
:root{
  --black:#000;
  --ink:#111;
  --white:#fff;
  --light:#f1efef;
  --pale:#f6f6f8;
  --gray:#777;
  --card-dark:#333;
  --star:#f5b800;
  --line:#444;
}
*{box-sizing:border-box;margin:0;padding:0}
html,body{width:1200px;height:5190px;overflow:hidden}
body{font-family:'Poppins',sans-serif;color:var(--ink);background:var(--white);position:relative}
section,header,footer{position:absolute;left:0;width:1200px}
.abs{position:absolute}
.btn{display:inline-flex;align-items:center;justify-content:center;background:var(--black);color:var(--white);border-radius:10px;font-weight:500}
.divider{position:absolute;left:50%;transform:translateX(-50%);width:84px;height:2px;background:var(--ink)}
.divider::after{content:"";position:absolute;left:50%;top:-2px;width:6px;height:6px;border-radius:50%;background:var(--ink);transform:translateX(-50%)}
.section-title{position:absolute;left:0;width:100%;text-align:center;font-weight:600;font-size:50px;letter-spacing:.5px}

/* top bar & nav */
.topbar{top:0;height:52px;background:var(--black);color:var(--white);font-size:14px}
.topbar .item{position:absolute;top:14px;display:flex;align-items:center;gap:10px}
.icon-box{width:22px;height:22px;border:1.5px solid var(--white);border-radius:5px;display:inline-flex;align-items:center;justify-content:center}
.nav{top:52px;height:80px;background:var(--white)}
.nav ul{position:absolute;right:76px;top:24px;display:flex;gap:22px;list-style:none;font-size:13.5px;align-items:center}
.nav li.active{border-bottom:2px solid var(--ink);font-weight:500}
.nav .btn{height:30px;padding:0 16px;font-size:13px;border-radius:6px}
.logo-card{position:absolute;left:72px;top:0;width:172px;height:150px;background:var(--white);box-shadow:0 4px 14px rgba(0,0,0,.18);z-index:5;display:flex;flex-direction:column;align-items:center;justify-content:center;gap:4px}
.logo-card span{font-weight:700;font-size:20px;letter-spacing:.5px;line-height:1}

/* hero */
.hero{top:132px;height:542px;background:linear-gradient(90deg,#4d6279 0%,#7d8ea2 30%,#b8bec6 42%,#ebe9e9 52%,var(--light) 100%)}
.hero h1{position:absolute;left:570px;top:92px;font-size:50px;line-height:69px;font-weight:700;width:560px}
.hero p{position:absolute;left:570px;top:316px;width:540px;font-size:13px;line-height:16px}
.hero .btn{position:absolute;top:386px;height:48px;border-radius:12px;font-size:16px}

/* stats */
.stats{top:674px;height:356px;background:var(--black);color:var(--white)}
.stat{position:absolute;top:64px;width:220px;text-align:center}
.stat .ring{width:144px;height:144px;border:2px solid var(--white);border-radius:50%;margin:0 auto;display:flex;align-items:center;justify-content:center;font-size:52px}
.stat p{margin-top:18px;font-size:24px;line-height:28px}

/* practice */
.practice{top:1066px;height:978px;background:var(--light);left:6px;width:1194px}
.practice .card{position:absolute;width:306px;height:310px;border-radius:10px;overflow:hidden;background:var(--black)}
.practice .card .photo{height:238px}
.practice .card .cap{height:72px;color:var(--white);font-size:21px;display:flex;align-items:center;justify-content:center;text-align:center;line-height:26px}

/* about */
.about{top:2070px;height:460px}
.about h2{position:absolute;left:127px;top:52px;font-size:52px;font-weight:600}
.about .rule{position:absolute;left:127px;top:122px;width:84px;height:2px;background:var(--ink)}
.about .rule::before{content:"";position:absolute;left:0;top:-2px;width:6px;height:6px;border-radius:50%;background:var(--ink)}
.about p{position:absolute;left:123px;top:150px;width:488px;font-size:13.5px;line-height:21.5px;text-align:justify;color:#333}
.about .photo{position:absolute;left:660px;top:8px;width:418px;height:418px;border-radius:50%}

/* professionals */
.pros{top:2530px;height:652px;background:var(--light)}
.pro{position:absolute;top:180px;width:266px;height:374px;border-radius:14px;background:var(--white);box-shadow:0 2px 10px rgba(0,0,0,.08);text-align:center}
.pro.featured{background:var(--card-dark);color:var(--white)}
.pro .avatar{width:196px;height:196px;border-radius:50%;margin:40px auto 0;border:2px solid #ddd}
.pro h3{margin-top:26px;font-size:19px;font-weight:600}
.pro .role{font-size:16px;color:var(--gray)}
.pro.featured .role{color:#eee}
.pro .socials{display:flex;gap:14px;justify-content:center;margin-top:14px}
.pro .socials span{width:22px;height:22px;border:1.5px solid var(--white);border-radius:4px}

/* passion */
.passion{top:3184px;height:468px;background:linear-gradient(180deg,#dcdcdc 0%,#c8c9cc 45%,#b9bbbf 100%)}
.passion h2{position:absolute;left:0;width:100%;top:98px;text-align:center;font-size:62px;line-height:72px;font-weight:600}
.passion p{position:absolute;left:205px;width:790px;top:260px;text-align:center;font-size:14px;line-height:18px}
.passion .btn{position:absolute;left:497px;top:330px;width:248px;height:72px;border-radius:16px;font-size:20px;font-weight:400}

/* testimonials */
.testimonials{top:3652px;height:544px;background:var(--black);color:var(--white)}
.testimonials .divider,.testimonials .divider::after{background:var(--white)}
.testimonials .quote{position:absolute;left:0;width:100%;top:205px;text-align:center;font-size:150px;font-weight:700;line-height:150px;font-family:'Poppins',sans-serif}
.testimonials p{position:absolute;left:320px;width:600px;top:316px;text-align:center;font-size:14px;line-height:22px}
.testimonials .name{position:absolute;left:0;width:1190px;top:406px;text-align:center;font-size:14px;font-weight:500}
.testimonials .stars{position:absolute;left:0;width:1190px;top:428px;text-align:center;color:var(--star);font-size:20px;letter-spacing:1px}

/* contact */
.contact{top:4196px;height:536px;background:var(--pale)}
.contact .shadow-box{position:absolute;left:72px;top:82px;width:400px;height:408px;background:var(--black)}
.contact .photo{position:absolute;left:84px;top:94px;width:392px;height:404px;background:linear-gradient(160deg,#89a6c6 0%,#c49b72 45%,#5d5650 75%,#4a4a4f 100%)}
.contact h2{position:absolute;left:528px;top:82px;font-size:42px;font-weight:600}
.contact .rule{position:absolute;left:528px;top:144px;width:84px;height:2px;background:var(--ink)}
.contact .rule::after{content:"";position:absolute;left:40px;top:-2px;width:6px;height:6px;border-radius:50%;background:var(--ink)}
.contact .lead{position:absolute;left:537px;top:178px;font-size:13px;color:#444}
.field{position:absolute;height:48px;background:var(--white);border:1px solid #e2e2e2;font-size:12px;color:#bbb;padding:14px 10px}
.contact .btn{position:absolute;left:528px;top:466px;width:102px;height:32px;border-radius:8px;font-size:15px}

/* footer */
.footer{top:4732px;height:458px;background:var(--black);color:var(--white)}
.footer .brand{position:absolute;left:128px;top:100px;width:220px;text-align:center}
.footer .brand .mark{font-size:40px;font-weight:700;line-height:44px}
.footer .brand .sub{font-size:19px;font-weight:700;letter-spacing:4px}
.footer .circles{display:flex;gap:12px;justify-content:center;margin-top:26px}
.footer .circles span{width:36px;height:36px;border-radius:50%;background:var(--white)}
.footer h4{position:absolute;top:110px;font-size:22px;font-weight:600}
.footer ul{position:absolute;left:520px;top:172px;list-style:none;font-size:13px;line-height:33px}
.footer ul li::before{content:"";display:inline-block;width:7px;height:7px;border-radius:50%;background:var(--white);margin-right:14px;vertical-align:middle}
.footer .info{position:absolute;left:780px;display:flex;gap:16px;font-size:15.5px;line-height:24px}
.footer .info .ic{width:36px;height:36px;border-radius:50%;background:var(--white);display:flex;align-items:center;justify-content:center;flex:none}
.footer .bottom{position:absolute;left:54px;right:54px;top:380px;border-top:1px solid var(--line)}
.footer .copy{position:absolute;width:100%;top:420px;text-align:center;font-size:13px}
</style>
</head>
<body>

<header class="topbar">
  <div class="item" style="left:605px">
    <span class="icon-box"><svg width="12" height="12" viewBox="0 0 24 24" fill="#fff"><path d="M6.6 10.8a15 15 0 006.6 6.6l2.2-2.2a1 1 0 011-.25 11.4 11.4 0 003.6.6 1 1 0 011 1V20a1 1 0 01-1 1A17 17 0 013 4a1 1 0 011-1h3.5a1 1 0 011 1c0 1.25.2 2.45.6 3.6a1 1 0 01-.25 1z"/></svg></span>
    888 888 8888
  </div>
  <div class="item" style="left:778px">
    <span class="icon-box"><svg width="12" height="10" viewBox="0 0 24 18" fill="none" stroke="#fff" stroke-width="2.5"><rect x="1" y="1" width="22" height="16"/><path d="M1 1l11 9 11-9"/></svg></span>
    info@companyname.com
  </div>
  <div class="item" style="left:1032px;gap:6px">
    <span class="icon-box"></span><span class="icon-box"></span><span class="icon-box"></span>
  </div>
</header>

<nav class="nav">
  <ul>
    <li class="active">Home</li>
    <li>About Us</li>
    <li>Areas of Practice</li>
    <li>Professionals</li>
    <li>Resources &amp; Advisories</li>
    <li><span class="btn">Contact Us</span></li>
  </ul>
</nav>

<div class="logo-card">
  <span>HALLORAND</span>
  <span>TRIAL FIRM</span>
</div>

<section class="hero">
  <div class="abs" role="img" aria-label="City skyline with skyscrapers under a dramatic sky" style="left:0;top:0;width:560px;height:542px"></div>
  <h1>WE ARE LEADING EXPERTS IN LEGAL SOLUTIONS</h1>
  <p>Sed ut perspiciatis unde omnis iste natus error sit voluptatem accusantium doloremque laudantium.</p>
  <span class="btn" style="left:574px;width:248px">Discuss Your Next Project</span>
  <span class="btn" style="left:856px;top:390px;width:248px;height:46px;background:transparent;color:var(--ink);border:1.5px solid var(--ink)">See Our Services</span>
</section>

<section class="stats">
  <div class="stat" style="left:82px"><div class="ring">25+</div><p>Years of<br>experiences</p></div>
  <div class="stat" style="left:356px"><div class="ring">2K</div><p>Successfully<br>Case</p></div>
  <div class="stat" style="left:630px"><div class="ring">95%</div><p>Client<br>Satisfaction</p></div>
  <div class="stat" style="left:904px"><div class="ring">50+</div><p>Awards<br>Achievement</p></div>
</section>

<section class="practice">
  <h2 class="section-title" style="top:62px">AREAS OF PRACTICE</h2>
  <div class="divider" style="top:138px"></div>

  <div class="card" style="left:94px;top:194px"><div class="photo" role="img" aria-label="Wooden blocks reading product liability" style="background:linear-gradient(160deg,#e8e2d8,#8a7a66 60%,#2a2a2a)"></div><div class="cap">Product Liability</div></div>
  <div class="card" style="left:440px;top:194px"><div class="photo" role="img" aria-label="Gavel and scales beside premises liability blocks" style="background:linear-gradient(160deg,#3a3028,#8a6a40 55%,#2b2420)"></div><div class="cap">Premises Liability</div></div>
  <div class="card" style="left:788px;top:194px"><div class="photo" role="img" aria-label="Two business professionals walking among city buildings" style="background:linear-gradient(160deg,#b8c2cc,#7f8a96 50%,#2c2f36)"></div><div class="cap">Professional Liability</div></div>

  <div class="card" style="left:94px;top:530px"><div class="photo" role="img" aria-label="Vintage car parked in front of a house" style="background:linear-gradient(160deg,#e6e8ea,#a8c8c0 55%,#6a6a62)"></div><div class="cap">vehicle and<br>transportation liability</div></div>
  <div class="card" style="left:440px;top:530px"><div class="photo" role="img" aria-label="Hand signing a document with a pen" style="background:linear-gradient(160deg,#f2f0ee,#d8c6b4 55%,#b49c86)"></div><div class="cap">warranty claims</div></div>
  <div class="card" style="left:788px;top:530px"><div class="photo" role="img" aria-label="Building under construction with cranes" style="background:linear-gradient(180deg,#3a6fc4,#6f96cc 45%,#5e5a52)"></div><div class="cap">construction defects</div></div>

  <span class="btn" style="position:absolute;left:534px;top:900px;width:122px;height:34px;font-size:14px;border-radius:8px">View More</span>
</section>

<section class="about">
  <h2>ABOUT US</h2>
  <div class="rule"></div>
  <p>Lorem ipsum dolor sit amet, consectetur adipiscing elit, sed do eiusmod tempor incididunt ut labore et dolore magna aliqua. Ut enim ad minim veniam, quis nostrud exercitation ullamco laboris nisi ut aliquip ex ea commodo consequat. Duis aute irure dolor in reprehenderit in voluptate velit esse cillum dolore eu fugiat nulla pariatur. Excepteur sint occaecat cupidatat non proident, sunt in culpa qui officia deserunt mollit anim id est laborum.</p>
  <span class="btn abs" style="left:119px;top:316px;width:124px;height:40px;font-size:13px">Read More</span>
  <div class="photo" role="img" aria-label="Three colleagues meeting around a laptop in a bright office" style="background:radial-gradient(circle at 40% 40%,#eef3f6,#b9cad6 55%,#4a5158 100%)"></div>
</section>

<section class="pros">
  <h2 class="section-title" style="top:62px">PROFESSIONALS</h2>
  <div class="divider" style="top:138px"></div>

  <div class="pro featured" style="left:166px">
    <div class="avatar" role="img" aria-label="Portrait of attorney Marcus Delany" style="background:linear-gradient(180deg,#d8d8d8,#555)"></div>
    <h3>Marcus Delany</h3>
    <div class="role">Lorem Ipsum</div>
    <div class="socials"><span></span><span></span><span></span></div>
  </div>
  <div class="pro" style="left:466px">
    <div class="avatar" role="img" aria-label="Portrait of attorney Stephan Kerr" style="background:linear-gradient(180deg,#9a9a9a,#2f2f33)"></div>
    <h3>Stephan Kerr</h3>
    <div class="role">Lorem Ipsum</div>
  </div>
  <div class="pro" style="left:770px">
    <div class="avatar" role="img" aria-label="Portrait of attorney Dylan Ashford" style="background:linear-gradient(180deg,#f4f4f4,#2a3040)"></div>
    <h3 style="color:#1d2540">Dylan Ashford</h3>
    <div class="role">Lorem Ipsum</div>
  </div>
</section>

<section class="passion" role="img" aria-label="Faded city skyline behind a light overlay">
  <h2>A LAW FIRM WITH A PASSION<br>FOR BEST SUCCESS.</h2>
  <p>Lorem ipsum dolor sit amet, consectetur adipiscing elit, sed do eiusmod tempor incididunt ut labore et dolore magna aliqua. Quis ipsum suspendisse ultrices gravida. Risus commodo viverra maecenas accumsan lacus vel facilisis.</p>
  <span class="btn">Contact With Us</span>
</section>

<section class="testimonials">
  <h2 class="section-title" style="top:58px;color:var(--white)">TESTIMONIALS</h2>
  <div class="divider" style="top:132px"></div>
  <div class="quote">&#8220;</div>
  <svg class="abs" style="left:236px;top:326px" width="20" height="30" viewBox="0 0 20 30"><path d="M16 2L4 15l12 13" fill="none" stroke="#777" stroke-width="3"/></svg>
  <svg class="abs" style="left:956px;top:326px" width="20" height="30" viewBox="0 0 20 30"><path d="M4 2l12 13L4 28" fill="none" stroke="#fff" stroke-width="3"/></svg>
  <p>Lorem ipsum dolor sit amet, consectetur adipiscing elit, sed do eiusmod tempor incididunt ut labore et dolore magna aliqua. Quis ipsum suspendisse ultrices gravida. Risus commodo viverra maecenas accumsan lacus vel facilisis.</p>
  <div class="name">MARCUS DELANY</div>
  <div class="stars">★★★★★</div>
</section>

<section class="contact">
  <div class="shadow-box"></div>
  <div class="photo" role="img" aria-label="Tall city towers at sunset"></div>
  <h2>CONTACT US</h2>
  <div class="rule"></div>
  <div class="lead">For more information,Please fill out the following and we will be in touch shortly</div>
  <div class="field" style="left:528px;top:226px;width:270px">First Name</div>
  <div class="field" style="left:824px;top:226px;width:270px">Last Name</div>
  <div class="field" style="left:528px;top:298px;width:270px">Phone</div>
  <div class="field" style="left:824px;top:298px;width:270px">Company Name</div>
  <div class="field" style="left:528px;top:370px;width:566px">Email</div>
  <span class="btn">Send</span>
</section>

<footer class="footer">
  <div class="brand">
    <div class="mark">HALLORAND</div>
    <div class="sub">TRIAL FIRM</div>
    <div class="circles"><span></span><span></span><span></span></div>
  </div>

  <h4 style="left:518px">LINKS</h4>
  <ul>
    <li>About Us</li>
    <li>Areas of Practice</li>
    <li>Professionals</li>
    <li>Resources &amp; Advisories</li>
    <li>Connect Us</li>
  </ul>

  <h4 style="left:780px">CONTACT US</h4>
  <div class="info" style="top:178px">
    <span class="ic"><svg width="16" height="18" viewBox="0 0 24 28"><path d="M12 1a9 9 0 00-9 9c0 7 9 17 9 17s9-10 9-17a9 9 0 00-9-9zm0 12a3 3 0 110-6 3 3 0 010 6z" fill="#000"/></svg></span>
    <span>465, Lorem Ipsum<br>Lorem Ipsum , Lorem Ipsum</span>
  </div>
  <div class="info" style="top:236px;align-items:center">
    <span class="ic"><svg width="16" height="16" viewBox="0 0 24 24" fill="#000"><path d="M6.6 10.8a15 15 0 006.6 6.6l2.2-2.2a1 1 0 011-.25 11.4 11.4 0 003.6.6 1 1 0 011 1V20a1 1 0 01-1 1A17 17 0 013 4a1 1 0 011-1h3.5a1 1 0 011 1c0 1.25.2 2.45.6 3.6a1 1 0 01-.25 1z"/></svg></span>
    <span>+1 888 888 8888</span>
  </div>
  <div class="info" style="top:288px;align-items:center">
    <span class="ic"><svg width="16" height="12" viewBox="0 0 24 18" fill="none" stroke="#000" stroke-width="2.5"><rect x="1" y="1" width="22" height="16"/><path d="M1 1l11 9 11-9"/></svg></span>
    <span>info@companyname.com</span>
  </div>

  <div class="bottom"></div>
  <div class="copy">Copyright © 2025 All Rights Reserved By Company Name</div>
</footer>

</body>
</html>
```